Website and rebrand- Makeup Artist

I need a new website built, new logo and email hosting. I'm rebranding to: MAELIS DUVANKE, Makeup. I need the following pages to showcase my services: main/home, about, gallery, frequently asked questions, contact, scrolling/streaming testimonials & live stream to my Instagram account.
I'm looking for a clean, fuss-free site to show off my images. Must be fashion forward and sophisticated. I would like a light and bright feel to the site which is quite different to my current website.
Original/current website is: www.maelisorvick.com

My domain and logo needs to change to: Maelis Duvanke, Hair & Makeup.

Inspiration:
www.harbelfaces.com.au
www.noraquillet.com.au (i love this simple layout!)
www.lyssavondraike.com
www.odettebrunsvik.com
Updates

inspiration for website and logo:www.noraquillet.com.au Added Sunday, March 8, 2015

Target Market(s)

Females aged 20-40

Industry/Entity Type

Fashion

Number of Pages Required

5+ page

Font styles to use
Sans Serif

Requirements
Must have
• Gallery
• Contact page
• Bio/about me
• Clear, sophisticated logo
• Email hosting, eg: info@maelisduvanke.com
• Compatable with tablets and smart phones.
Nice to have
• Constant stream of testimonials
• Live feed from social media accounts.
• Movement in pages
• Videos of me (pulled from YouTube)
Should not have
• Child like colours and font design
• Cluttered pages

```html
<!DOCTYPE html>
<html lang="en">
<head>
<meta charset="utf-8">
<title>Maelis Duvanke · Hair &amp; Makeup</title>
<link rel="stylesheet" href="https://fonts.googleapis.com/css2?family=Teko:wght@500;600&family=Roboto:wght@300;400&family=Open+Sans:wght@400&display=swap">
<style>
  :root{
    --ink:#2b2b2b;
    --nav:#444;
    --rule:#b3b3b3;
    --hero-deep:#1e0f3a;
    --hero-mid:#4a2e72;
    --hero-skin:#8a6a80;
    --card-bg:#f8f8f8;
    --card-line:#e6e6e6;
    --footer:#111111;
    --footer-text:#b9b9b9;
    --accent:#1fb7b0;
    --icon:#c9c9c9;
  }
  *{box-sizing:border-box;margin:0;padding:0}
  html,body{width:1200px;height:1166px;overflow:hidden;background:#fff}
  body{position:relative;font-family:"Open Sans",sans-serif;color:var(--ink)}

  .site-header{position:absolute;left:0;top:0;width:1200px;height:103px;background:#fff}
  .brand{position:absolute;left:98px;top:22px;font-family:"Teko",sans-serif;font-weight:600;font-size:52px;line-height:1;color:var(--ink);letter-spacing:.5px}
  .main-nav{position:absolute;right:99px;top:45px;display:flex;gap:42px;font-family:"Roboto",sans-serif;font-size:15.5px;color:var(--nav)}
  .main-nav a{color:inherit;text-decoration:none;position:relative}
  .main-nav a.current::before{content:"";position:absolute;left:0;top:-45px;width:41px;height:3px;background:var(--rule)}

  .hero{position:absolute;left:0;top:103px;width:1200px;height:621px;overflow:hidden;
    background:
      radial-gradient(ellipse 300px 380px at 380px 300px, var(--hero-skin) 0%, rgba(90,60,100,.6) 45%, transparent 75%),
      radial-gradient(ellipse 600px 500px at 900px 250px, #5b3f86 0%, transparent 70%),
      linear-gradient(90deg, var(--hero-deep) 0%, var(--hero-mid) 50%, #2a1550 100%);}
  .hero-title{position:absolute;right:99px;text-align:right;color:#fff;font-family:"Teko",sans-serif;font-weight:600;line-height:1}
  .hero-title .name{position:absolute;right:0;top:-6px;font-size:46px;white-space:nowrap}
  .hero-title .service{position:absolute;right:0;top:36px;font-size:100px;white-space:nowrap}
  .hero-arrow{position:absolute;top:287px;width:46px;height:46px}

  .section-title{position:absolute;top:754px;font-family:"Roboto",sans-serif;font-weight:300;font-size:21px;color:#333;letter-spacing:.3px}

  .insta-grid{position:absolute;left:99px;top:799px;width:330px;height:254px;display:grid;grid-template-columns:repeat(3,1fr);grid-template-rows:repeat(3,1fr);gap:3px}
  .insta-grid div{border-radius:1px}

  .testimonial{position:absolute;left:459px;width:310px;height:81px;background:var(--card-bg);border:1px solid var(--card-line)}
  .testimonial .avatar{position:absolute;left:10px;top:15px;width:36px;height:36px;border-radius:4px;background:linear-gradient(160deg,#3a80c4,#1f4d86)}
  .testimonial blockquote{position:absolute;left:61px;top:12px;width:240px;font-size:10.5px;line-height:17px;color:#444}
  .testimonial cite{position:absolute;left:61px;top:54px;font-style:normal;font-size:11.5px;color:#222}

  .video{position:absolute;left:798px;top:799px;width:304px;height:252px;background:linear-gradient(90deg,#d8cbbd 0 32%,#1d1d1d 32% 100%)}
  .video .play{position:absolute;left:95px;top:87px}
  .video .bar{position:absolute;left:0;bottom:0;width:304px;height:22px;background:#1b1b1b;font-family:"Roboto",sans-serif;font-size:7px;color:#888}
  .video .progress{position:absolute;left:0;bottom:22px;width:304px;height:4px;background:#555}
  .video .progress span{position:absolute;left:0;top:0;width:188px;height:4px;background:#d0101a}

  .site-footer{position:absolute;left:0;top:1095px;width:1200px;height:71px;background:var(--footer)}
  .copyright{position:absolute;left:100px;top:26px;font-size:13.5px;color:var(--footer-text)}
  .social{position:absolute;left:888px;top:27px;display:flex;gap:17px}
  .social span{width:16px;height:16px;border-radius:50%;background:var(--icon)}
  .social span:first-child{background:var(--accent)}
</style>
</head>
<body>

<header class="site-header">
  <div class="brand">Maelis Duvanke</div>
  <nav class="main-nav">
    <a class="current" href="#">HOME</a>
    <a href="#">ABOUT</a>
    <a href="#">GALLERY</a>
    <a href="#">FAQ</a>
    <a href="#">CONTACT</a>
  </nav>
</header>

<section class="hero" role="img" aria-label="Portrait of a woman with long dark curls and dramatic eye makeup against a purple bokeh background">
  <svg class="hero-arrow" style="left:25px" viewBox="0 0 46 46" aria-hidden="true">
    <circle cx="23" cy="23" r="22" fill="none" stroke="rgba(255,255,255,.45)" stroke-width="1.5"/>
    <path d="M26 14 L17 23 L26 32" fill="none" stroke="rgba(255,255,255,.8)" stroke-width="4" stroke-linecap="round" stroke-linejoin="round"/>
  </svg>
  <svg class="hero-arrow" style="left:1128px" viewBox="0 0 46 46" aria-hidden="true">
    <circle cx="23" cy="23" r="22" fill="none" stroke="rgba(255,255,255,.45)" stroke-width="1.5"/>
    <path d="M20 14 L29 23 L20 32" fill="none" stroke="rgba(255,255,255,.8)" stroke-width="4" stroke-linecap="round" stroke-linejoin="round"/>
  </svg>
  <div class="hero-title" style="top:272px">
    <div class="name">Maelis Duvanke</div>
    <div class="service">Hair &amp; Makeup</div>
  </div>
</section>

<h2 class="section-title" style="left:97px">INSTAGRAM</h2>
<h2 class="section-title" style="left:456px">TESTIMONIALS</h2>
<h2 class="section-title" style="left:795px">FEATURE VIDEO</h2>

<div class="insta-grid">
  <div role="img" aria-label="Makeup brush being applied to a cheek" style="background:linear-gradient(135deg,#e9d8cc,#b58a70)"></div>
  <div role="img" aria-label="Bridal portrait with soft curls" style="background:linear-gradient(135deg,#eeeae6,#8d7a6e)"></div>
  <div role="img" aria-label="Model with voluminous curls and violet eyeshadow" style="background:linear-gradient(135deg,#d5c6d8,#5b3c58)"></div>
  <div role="img" aria-label="Blue smoky eye and painted nails" style="background:linear-gradient(135deg,#e2d4c8,#2d3f6e)"></div>
  <div role="img" aria-label="Natural blonde beauty look" style="background:linear-gradient(135deg,#f1e4d4,#c9a783)"></div>
  <div role="img" aria-label="Romantic auburn hairstyle" style="background:linear-gradient(135deg,#e0c49a,#7a4a2c)"></div>
  <div role="img" aria-label="Long golden waves" style="background:linear-gradient(135deg,#e6d3bd,#9a6b42)"></div>
  <div role="img" aria-label="Hair being styled with a comb" style="background:linear-gradient(135deg,#cfc4bb,#2c2624)"></div>
  <div role="img" aria-label="Eyeliner application on a bride" style="background:linear-gradient(135deg,#f3ece4,#b89c7c)"></div>
</div>

<article class="testimonial" style="top:799px">
  <div class="avatar" role="img" aria-label="Client avatar"></div>
  <blockquote>“ Lorem ipsum dolor sit amet, consectetur adipiscing elit, sed do Lorem ipsum dolor sit ”</blockquote>
  <cite>Dorian Pellew</cite>
</article>
<article class="testimonial" style="top:885px">
  <div class="avatar" role="img" aria-label="Client avatar"></div>
  <blockquote>“ Lorem ipsum dolor sit amet, consectetur adipiscing elit, sed do Lorem ipsum dolor sit ”</blockquote>
  <cite>Dorian Pellew</cite>
</article>
<article class="testimonial" style="top:970px">
  <div class="avatar" role="img" aria-label="Client avatar"></div>
  <blockquote>“ Lorem ipsum dolor sit amet, consectetur adipiscing elit, sed do Lorem ipsum dolor sit ”</blockquote>
  <cite>Dorian Pellew</cite>
</article>

<div class="video" role="img" aria-label="Video still of a makeup artist interviewed at a fashion event">
  <svg class="play" width="68" height="68" viewBox="0 0 68 68" aria-hidden="true">
    <circle cx="34" cy="34" r="31" fill="rgba(255,255,255,.12)" stroke="rgba(255,255,255,.6)" stroke-width="4"/>
    <path d="M26 20 L50 34 L26 48 Z" fill="rgba(255,255,255,.6)"/>
  </svg>
  <div class="progress"><span></span></div>
  <svg style="position:absolute;left:183px;bottom:17px" width="12" height="12" aria-hidden="true"><circle cx="6" cy="6" r="5" fill="#ddd"/></svg>
  <div class="bar">
    <svg style="position:absolute;left:18px;top:6px" width="10" height="10" aria-hidden="true"><rect x="1" y="1" width="3" height="9" fill="#aaa"/><rect x="6" y="1" width="3" height="9" fill="#aaa"/></svg>
    <svg style="position:absolute;left:49px;top:6px" width="14" height="10" aria-hidden="true"><path d="M1 3 H4 L8 0 V10 L4 7 H1 Z" fill="#ddd"/><path d="M10 2 Q13 5 10 8" stroke="#ddd" fill="none"/></svg>
    <svg style="position:absolute;left:70px;top:9px" width="40" height="6" aria-hidden="true"><rect x="0" y="1" width="38" height="2" fill="#555"/><rect x="0" y="1" width="28" height="2" fill="#c0101a"/><rect x="27" y="0" width="3" height="6" fill="#ddd"/></svg>
    <span style="position:absolute;left:119px;top:7px">2:43 / 4:26</span>
    <span style="position:absolute;left:250px;top:7px">360p</span>
    <svg style="position:absolute;left:285px;top:6px" width="10" height="10" aria-hidden="true"><path d="M1 4 V1 H4 M6 1 H9 V4 M9 6 V9 H6 M4 9 H1 V6" stroke="#aaa" fill="none"/></svg>
  </div>
</div>

<footer class="site-footer">
  <p class="copyright">© 2015 MAELIS ORVICK. All rights reserved.</p>
  <div class="social" aria-label="Social links">
    <span role="img" aria-label="Social link"></span>
    <span role="img" aria-label="Social link"></span>
    <span role="img" aria-label="Social link"></span>
    <span role="img" aria-label="Social link"></span>
    <span role="img" aria-label="Social link"></span>
    <span role="img" aria-label="Social link"></span>
    <span role="img" aria-label="Social link"></span>
  </div>
</footer>

</body>
</html>
```